Destination Wedding Photographer

I am a Wedding photographer based in San Juan, Puerto Rico. The banner will be shown in the United States to brides that plan to have their wedding in Puerto Rico.

I want to highlight the following words/phrases
Puerto Rico
Destination Wedding
Photographer
(in that order)

feel free to get creative adding your own inspired text.

My web site: www.benitolavarro.com

Target Market(s)

Brides in the united states looking for a photographer for their wedding in Puerto Rico

Industry/Entity Type

Wedding

Requirements
Must have
• + Your ad must be a .gif, .png or .jpg smaller than 40kb in filesize
+ include the following sizes: 300x250, 728x90, 160x600, 468x60, or 120x600
+ Your ad must include the advertiser's brand
+ Your ad must have a border
Should not have
• + Your ad cannot imitate computer effects like scrolling or mousing over
+ No animations longer than 30 seconds
+ No strobe or flashing effects allowed
+ Your ad and campaign must not feature or promote alcohol, anabolic steroids, drugs, financial products, gambling, adult content, or weight loss products

```html
<!DOCTYPE html>
<html lang="en">
<head>
<meta charset="utf-8">
<title>Benito Lavarro Photography — Puerto Rico Destination Wedding Photographer</title>
<link href="https://fonts.googleapis.com/css2?family=Quicksand:wght@300;400&family=Open+Sans:ital,wght@1,600&display=swap" rel="stylesheet">
<style>
  :root {
    --canvas: #ffffff;
    --frame: #9a9a9a;
    --sky-top: #dfe6ec;
    --sky-low: #eef2f5;
    --horizon: #8fb3c9;
    --sea-top: #3f7fa6;
    --sea-low: #2a5f82;
    --title-grey: #a9b2b9;
    --brand-grey: #6a6d70;
    --tagline: #ffffff;
  }
  html, body {
    margin: 0;
    padding: 0;
    width: 1200px;
    height: 320px;
    overflow: hidden;
    background: var(--canvas);
  }
  .banner {
    position: relative;
    box-sizing: border-box;
    width: 1200px;
    height: 320px;
    border: 4px solid var(--canvas);
    outline: 2px solid var(--frame);
    outline-offset: -4px;
    overflow: hidden;
  }
  .banner__scene {
    position: absolute;
    inset: 0;
    background: linear-gradient(
      to bottom,
      var(--sky-top) 0%,
      var(--sky-low) 66%,
      var(--horizon) 71%,
      var(--sea-top) 74%,
      var(--sea-low) 100%
    );
  }
  .banner__place {
    position: absolute;
    left: 36px;
    top: 18px;
    margin: 0;
    font-family: "Quicksand", sans-serif;
    font-weight: 400;
    font-size: 46px;
    letter-spacing: -0.5px;
    color: var(--title-grey);
  }
  .brand {
    position: absolute;
    right: 40px;
    top: 78px;
    width: 420px;
    text-align: center;
    font-family: "Quicksand", sans-serif;
    font-weight: 300;
    color: var(--brand-grey);
  }
  .brand__name {
    display: block;
    font-size: 60px;
    line-height: 1;
  }
  .brand__trade {
    display: block;
    margin-top: 14px;
    font-size: 20px;
    letter-spacing: 7px;
    text-transform: uppercase;
  }
  .banner__tagline {
    position: absolute;
    right: 36px;
    top: 238px;
    margin: 0;
    font-family: "Open Sans", sans-serif;
    font-style: italic;
    font-weight: 600;
    font-size: 23px;
    color: var(--tagline);
  }
</style>
</head>
<body>
  <section class="banner">
    <div class="banner__scene" role="img" aria-label="Photo of a man kneeling to propose to a woman in a red dress on a seaside cliff in Puerto Rico, with pale sky and blue ocean behind them"></div>
    <h1 class="banner__place">Puerto Rico</h1>
    <div class="brand">
      <span class="brand__name">Benito Lavarro</span>
      <span class="brand__trade">Photography</span>
    </div>
    <p class="banner__tagline">Destination Wedding Photographer</p>
  </section>
</body>
</html>
```